Creation of a page for funnel

Our company is specialized in insoles and well-being. Our insoles help reduce joint problems, stress or ink to promote weight loss. We need a clean and refined sales page, this one will be used on funnel click. The page should display the values of our product in first: "promote weight loss" in second: "Relieves muscle and joint pain" third: "Increases energy and stress stress". The page must be in the colors of our logo (green) if possible this color: light green: dark green 54c248. It is important to follow this model for the page with totally new and fresh desing: https: // lunavera-shop. uk / kto-rb Additionnal details for icons Section u: 1: "A unique design based on two types of knowledge" 2: "approved by acupressure expert" "Lose weight" 2: "Increases blood flow and oxygen in your body" 3: "Relieves muscle and joint pain" 4: "Increases energy and reduces stress" Section x: 1: "for men and women" 2: "one size "3:" Adjustable by cutting "Section y: 1:" powerful magnet in tourmaline "2:" for all type of shoes "3:" Flexible and light "4:" Breathable "Section z: 1:" free shipping "2 : "Customer service" 3: "money back guarantee" 4: "safe payment"
Target Market(s)
men and women 35
Number of Pages Required
1 page
Requirements
Must have
- the 5 sections mentioned in description
Nice to have
- some GIF like the funnel

```html
<!DOCTYPE html>
<html lang="en">
<head>
<meta charset="utf-8">
<title>StrideWell – Insoles for Well-being</title>
<link rel="stylesheet" href="https://fonts.googleapis.com/css2?family=Work+Sans:wght@500;600;700&family=Noto+Serif:wght@400;700&display=swap">
<style>
:root{
  --green:#54c248;
  --purple:#6a3cf5;
  --purple-deep:#7b2ff0;
  --ink:#111111;
  --body:#333333;
  --white:#ffffff;
  --card-shadow:0 6px 22px rgba(40,30,90,.09);
  --footer-bg:#eefbea;
  --heading:"Work Sans",Arial,sans-serif;
  --text:"Noto Serif",Georgia,serif;
}
*{box-sizing:border-box;margin:0;padding:0}
html,body{width:1200px;height:3304px;overflow:hidden}
body{position:relative;background:var(--white);font-family:var(--text);color:var(--body)}
.abs{position:absolute}
.backdrop{position:absolute;left:0;top:0;width:1200px;height:3304px}

/* header */
.site-header{position:absolute;left:0;top:0;width:1200px;height:62px;background:var(--white);z-index:3}
.brand{position:absolute;display:flex;align-items:center;gap:8px}
.brand-dot{width:18px;height:18px;border-radius:50%;background:var(--green)}
.brand-name{font-family:var(--heading);font-weight:700;font-size:22px;color:var(--ink);line-height:1}
.brand-tag{font-family:var(--heading);font-size:8px;color:var(--ink);margin-left:26px;margin-top:2px}
.main-nav a{position:absolute;top:23px;font-family:var(--heading);font-size:13px;font-weight:500;color:var(--ink);text-decoration:none}
.btn{position:absolute;display:flex;align-items:center;justify-content:center;background:var(--green);color:var(--white);font-family:var(--heading);font-weight:600;font-size:13px;border-radius:2px;text-decoration:none}

/* hero */
.hero-title{left:51px;top:214px;width:460px;font-family:var(--heading);font-weight:700;font-size:28px;line-height:44px;color:var(--white)}
.hero-list{left:51px;top:315px;list-style:none}
.hero-list li{display:flex;align-items:center;gap:14px;height:42px;font-size:14px;color:var(--white)}
.tick{width:16px;height:16px;flex:none}
.insole-visual{left:662px;top:204px;width:395px;height:344px;border-radius:48% 40% 46% 44%;background:linear-gradient(150deg,#c9ccd6 0%,#7d8ea8 45%,#3f6fd8 75%,#f08a2c 100%);opacity:.9}

/* benefits */
.section-title{font-family:var(--heading);font-weight:700;font-size:26px;line-height:36px;color:var(--ink)}
.intro-copy{left:51px;top:975px;width:360px;font-size:13.5px;line-height:22px;color:var(--ink)}
.benefit-card{position:absolute;width:173px;height:234px;background:var(--white);border-radius:6px;box-shadow:var(--card-shadow);display:flex;flex-direction:column;align-items:center;justify-content:center;gap:18px;z-index:2}
.benefit-card span{font-family:var(--heading);font-weight:600;font-size:13px;color:var(--ink)}
.line-icon{width:40px;height:40px;fill:none;stroke:var(--green);stroke-width:2;stroke-linecap:round;stroke-linejoin:round}

/* walking */
.walk-title{left:0;top:1350px;width:1200px;text-align:center;font-family:var(--heading);font-weight:700;font-size:28px;color:var(--ink)}
.walk-title em{font-style:normal;color:var(--green)}
.feature-card{position:absolute;top:1424px;width:268px;height:237px;background:var(--white);border-radius:6px;box-shadow:var(--card-shadow);text-align:center;padding-top:26px;z-index:2}
.feature-card h3{margin-top:24px;font-family:var(--heading);font-weight:600;font-size:14px;color:var(--ink)}
.feature-card p{margin:10px auto 0;width:200px;font-size:13px;line-height:22px;color:var(--ink)}

/* advantages */
.pain-visual{left:143px;top:1873px;width:451px;height:593px;border-radius:6px;background:radial-gradient(circle at 45% 40%,#6b6b6b 0%,#333 55%,#151515 100%);z-index:2}
.adv-title{left:698px;top:1868px;width:360px;font-family:var(--heading);font-weight:700;font-size:28px;line-height:38px;color:var(--white);z-index:2}
.adv-item{position:absolute;left:698px;width:380px;z-index:2}
.adv-item h4{display:flex;align-items:center;gap:14px;font-family:var(--text);font-weight:400;font-size:13px;color:var(--white)}
.adv-item p{margin:10px 0 0 30px;font-size:11.5px;line-height:19px;color:var(--white)}

/* order */
.order-title{left:0;top:2762px;width:1200px;text-align:center;font-family:var(--heading);font-weight:700;font-size:28px;color:var(--ink)}
.order-title em{font-style:normal;color:var(--green)}
.service-card{position:absolute;width:268px;height:119px;background:var(--white);border-radius:6px;box-shadow:var(--card-shadow);display:flex;align-items:center;justify-content:center;gap:14px}
.service-card span{font-family:var(--heading);font-weight:600;font-size:14px;color:var(--ink)}
.service-card .line-icon{width:34px;height:34px}

/* footer */
.site-footer{position:absolute;left:0;top:3167px;width:1200px;height:137px;background:var(--footer-bg)}
.footer-col{position:absolute;top:38px}
.footer-col h5{font-family:var(--heading);font-weight:600;font-size:11px;color:var(--ink);margin-bottom:8px}
.footer-col a{display:block;font-size:10px;line-height:18px;color:var(--ink);text-decoration:none}
.social{position:absolute;top:65px;width:22px;height:22px;border-radius:3px}
</style>
</head>
<body>

<svg class="backdrop" viewBox="0 0 1200 3304" aria-hidden="true">
  <defs>
    <linearGradient id="purpleFill" x1="0" y1="0" x2="1" y2="1">
      <stop offset="0" stop-color="#6340f6"/>
      <stop offset="1" stop-color="#7d2cef"/>
    </linearGradient>
  </defs>
  <path fill="url(#purpleFill)" d="M0 62 H820 C900 62 930 150 1030 150 C1120 150 1200 130 1200 130 V560 C1200 620 1080 615 980 630 C860 648 800 760 700 790 C560 830 420 822 250 795 C150 778 60 762 0 770 Z"/>
  <path fill="url(#purpleFill)" d="M0 1690 C200 1650 500 1665 760 1642 C950 1625 1050 1560 1200 1572 V2598 C1100 2580 1000 2540 880 2560 C700 2590 560 2655 380 2632 C220 2612 100 2552 0 2540 Z"/>
</svg>

<header class="site-header">
  <div class="brand" style="left:51px;top:14px">
    <div class="brand-dot"></div><div class="brand-name">StrideWell</div>
  </div>
  <div class="abs brand-tag" style="left:51px;top:38px">walk feel better</div>
  <nav class="main-nav">
    <a href="#" style="left:438px">Home</a>
    <a href="#" style="left:515px">How it works?</a>
    <a href="#" style="left:645px">Pricing</a>
    <a href="#" style="left:731px">FAQs</a>
  </nav>
  <a class="btn" href="#" style="left:1040px;top:13px;width:74px;height:35px">Sign Up</a>
</header>

<section class="hero">
  <h1 class="abs hero-title">Lose Weight, Reduce Pain and Increase Energy</h1>
  <ul class="abs hero-list">
    <li><svg class="tick" viewBox="0 0 16 16"><circle cx="8" cy="8" r="7" fill="none" stroke="#fff" stroke-width="1.3"/><path d="M5 8.2l2 2 4-4" fill="none" stroke="#fff" stroke-width="1.3"/></svg>A totally natural solution without any health risk</li>
    <li><svg class="tick" viewBox="0 0 16 16"><circle cx="8" cy="8" r="7" fill="none" stroke="#fff" stroke-width="1.3"/><path d="M5 8.2l2 2 4-4" fill="none" stroke="#fff" stroke-width="1.3"/></svg>Approved by acupressure expert</li>
    <li><svg class="tick" viewBox="0 0 16 16"><circle cx="8" cy="8" r="7" fill="none" stroke="#fff" stroke-width="1.3"/><path d="M5 8.2l2 2 4-4" fill="none" stroke="#fff" stroke-width="1.3"/></svg>A unique design based on two types of knowledge</li>
  </ul>
  <a class="btn" href="#" style="left:51px;top:469px;width:135px;height:33px">Shop Now</a>
  <div class="abs insole-visual" role="img" aria-label="Product photo of a pair of orthopaedic insoles"></div>
</section>

<section class="benefits">
  <h2 class="abs section-title" style="left:51px;top:866px;width:340px">Safe and sustainable weight lose</h2>
  <p class="abs intro-copy">Some paragraph here that explains the use cases of this product. This will help the users understand this product and eventually but it.<br>This is placeholder text that has to be removed once the real data is ready. Some paragraph here that explains the use cases of this product. This will help the users understand this product and eventually but it. This is placeholder text that has to be removed once the real data is ready.</p>
  <a class="btn" href="#" style="left:273px;top:1246px;width:135px;height:31px">Shop Now</a>

  <div class="benefit-card" style="left:882px;top:611px">
    <svg class="line-icon" viewBox="0 0 40 40"><path d="M14 6c2 8 2 14-2 28M26 6c-2 8-2 14 2 28M16 18c3 2 5 2 8 0M18 26c2 1 3 1 4 0"/></svg>
    <span>Increases blood flow</span>
  </div>
  <div class="benefit-card" style="left:698px;top:703px">
    <svg class="line-icon" viewBox="0 0 40 40"><path d="M13 6v8c0 4 3 6 3 10v10M27 6v8c0 4-3 6-3 10v10M6 20h6M28 20h6M8 17l-3 3 3 3M32 17l3 3-3 3"/></svg>
    <span>Lose weight</span>
  </div>
  <div class="benefit-card" style="left:882px;top:869px">
    <svg class="line-icon" viewBox="0 0 40 40"><ellipse cx="20" cy="20" rx="9" ry="15" transform="rotate(40 20 20)"/><path d="M11 27l18-14M15 16l3 4M20 13l3 4M18 25l3 4"/></svg>
    <span>Relieves pain</span>
  </div>
  <div class="benefit-card" style="left:698px;top:961px">
    <svg class="line-icon" viewBox="0 0 40 40"><circle cx="20" cy="9" r="4"/><path d="M10 20l10-6 10 6M20 14v10l-6 10M20 24l6 10"/></svg>
    <span>Increases energy</span>
  </div>
</section>

<section class="walking">
  <h2 class="abs walk-title">Get better by walking <em>15 Minutes</em> everyday!</h2>
  <div class="feature-card" style="left:189px">
    <svg class="line-icon" viewBox="0 0 40 40"><circle cx="12" cy="8" r="3"/><circle cx="28" cy="8" r="3"/><path d="M8 34V16h8v18M24 34l-2-8 3-10h6l3 10-2 8"/></svg>
    <h3>For men and women</h3>
    <p>Some paragraph here that explains the use cases of this product.</p>
  </div>
  <div class="feature-card" style="left:466px">
    <svg class="line-icon" viewBox="0 0 40 40"><path d="M16 12c-4 6-4 14 0 20 3 4 9 3 9-2 0-5-4-6-3-12 1-4-4-10-6-6z"/><circle cx="20" cy="6" r="1.6"/><circle cx="24" cy="8" r="1.4"/><circle cx="27" cy="11" r="1.2"/></svg>
    <h3>One size</h3>
    <p>Some paragraph here that explains the use cases of this product.</p>
  </div>
  <div class="feature-card" style="left:744px">
    <svg class="line-icon" viewBox="0 0 40 40"><path d="M10 4v32M20 4v32M30 4v32"/><rect x="7" y="22" width="6" height="5"/><rect x="17" y="10" width="6" height="5"/><rect x="27" y="18" width="6" height="5"/></svg>
    <h3>Adjustable by cutting</h3>
    <p>Some paragraph here that explains the use cases of this product.</p>
  </div>
</section>

<section class="advantages">
  <div class="abs pain-visual" role="img" aria-label="Illustration of a seated figure with highlighted painful joints"></div>
  <h2 class="abs adv-title">What makes StrideWell better than others?</h2>
  <div class="adv-item" style="top:1970px">
    <h4><svg class="tick" viewBox="0 0 16 16"><circle cx="8" cy="8" r="7" fill="none" stroke="#fff" stroke-width="1.3"/><path d="M5 8.2l2 2 4-4" fill="none" stroke="#fff" stroke-width="1.3"/></svg>Powerful magnet in tourmaline</h4>
    <p>Some paragraph here that explains the use cases of this product. This will help the users understand this product and eventually buy it.</p>
  </div>
  <div class="adv-item" style="top:2077px">
    <h4><svg class="tick" viewBox="0 0 16 16"><circle cx="8" cy="8" r="7" fill="none" stroke="#fff" stroke-width="1.3"/><path d="M5 8.2l2 2 4-4" fill="none" stroke="#fff" stroke-width="1.3"/></svg>For all type of shoes</h4>
    <p>Some paragraph here that explains the use cases of this product. This will help the users understand this product and eventually buy it.</p>
  </div>
  <div class="adv-item" style="top:2184px">
    <h4><svg class="tick" viewBox="0 0 16 16"><circle cx="8" cy="8" r="7" fill="none" stroke="#fff" stroke-width="1.3"/><path d="M5 8.2l2 2 4-4" fill="none" stroke="#fff" stroke-width="1.3"/></svg>Flexible and light</h4>
    <p>Some paragraph here that explains the use cases of this product. This will help the users understand this product and eventually buy it.</p>
  </div>
  <div class="adv-item" style="top:2291px">
    <h4><svg class="tick" viewBox="0 0 16 16"><circle cx="8" cy="8" r="7" fill="none" stroke="#fff" stroke-width="1.3"/><path d="M5 8.2l2 2 4-4" fill="none" stroke="#fff" stroke-width="1.3"/></svg>Breathable</h4>
    <p>Some paragraph here that explains the use cases of this product. This will help the users understand this product and eventually buy it.</p>
  </div>
  <a class="btn" href="#" style="left:920px;top:2441px;width:135px;height:31px;z-index:2">Shop Now</a>
</section>

<section class="order">
  <h2 class="abs order-title">Order your <em>Stridewell</em> Now!</h2>
  <div class="service-card" style="left:326px;top:2836px">
    <svg class="line-icon" viewBox="0 0 34 34"><path d="M17 3l12 6v16l-12 6-12-6V9zM5 9l12 6 12-6M17 15v16"/></svg>
    <span>Free Shipping</span>
  </div>
  <div class="service-card" style="left:606px;top:2836px">
    <svg class="line-icon" viewBox="0 0 34 34"><circle cx="17" cy="12" r="6"/><path d="M6 31c0-7 5-11 11-11s11 4 11 11M9 13c0-5 4-9 8-9s8 4 8 9"/></svg>
    <span>24/7 Customer Service</span>
  </div>
  <div class="service-card" style="left:326px;top:2971px">
    <svg class="line-icon" viewBox="0 0 34 34"><path d="M29 17a12 12 0 1 1-4-9M25 3v5h5M20 12c-1-1-2-1.5-3-1.5-2 0-3.5 1-3.5 2.5 0 3.5 7 2 7 5.5 0 1.5-1.5 2.5-3.5 2.5-1.2 0-2.5-.5-3.3-1.5M17 9v2M17 21.5v2"/></svg>
    <span>Money Back Guarantee</span>
  </div>
  <div class="service-card" style="left:606px;top:2971px">
    <svg class="line-icon" viewBox="0 0 34 34"><rect x="4" y="9" width="26" height="17" rx="2"/><path d="M4 14h26M8 21h6"/></svg>
    <span>Secure Payment</span>
  </div>
</section>

<footer class="site-footer">
  <div class="brand" style="left:51px;top:56px">
    <div class="brand-dot"></div><div class="brand-name">StrideWell</div>
  </div>
  <div class="abs brand-tag" style="left:51px;top:80px">walk feel better</div>
  <div class="footer-col" style="left:232px"><h5>Useful Links</h5><a href="#">About Us</a><a href="#">How it works?</a><a href="#">FAQs</a></div>
  <div class="footer-col" style="left:418px"><h5>Study</h5><a href="#">Link 01</a><a href="#">Link 02</a><a href="#">Link 03</a></div>
  <div class="footer-col" style="left:604px"><h5>Support</h5><a href="#">Link 01</a><a href="#">Link 02</a><a href="#">Link 03</a></div>
  <div class="footer-col" style="left:790px"><h5>Partners</h5><a href="#">Link 01</a><a href="#">Link 02</a><a href="#">Link 03</a></div>
  <a class="social" href="#" aria-label="Social link one" style="left:976px;background:#3b5998"></a>
  <a class="social" href="#" aria-label="Social link two" style="left:1019px;background:#1da1f2"></a>
  <a class="social" href="#" aria-label="Social link three" style="left:1062px;background:#e1306c"></a>
</footer>

</body>
</html>
```